Environmental Group Website Template

We want a website template for an environmental cause. The website should have a dark content area that is transparent. The website text and icons are white.
The background is a nature scene. The background image repeats.
Industry/Entity Type
Group

```html
<!DOCTYPE html>
<html lang="en">
<head>
<meta charset="utf-8">
<title>Riverleaf Trust – Environmental Group</title>
<link rel="stylesheet" href="https://fonts.googleapis.com/css2?family=Roboto:wght@500;700&family=Open+Sans:wght@400;600&display=swap">
<style>
  :root {
    --sky-top: #6b3a4a;
    --sky-glow: #e2562a;
    --sky-warm: #f08a3a;
    --sea: #3a1d1a;
    --panel: rgba(18, 14, 16, 0.88);
    --panel-deep: rgba(8, 6, 8, 0.92);
    --card: rgba(20, 18, 20, 0.92);
    --accent: #8cc714;
    --text: #ffffff;
    --muted: #c9c4c2;
    --line: #6f6a6a;
  }
  * { box-sizing: border-box; margin: 0; padding: 0; }
  html, body { width: 1049px; height: 1200px; overflow: hidden; }
  body {
    position: relative;
    font-family: "Open Sans", Arial, sans-serif;
    color: var(--text);
    background: #1c1214;
  }
  .backdrop {
    position: absolute; inset: 0;
    background:
      linear-gradient(180deg, var(--sky-top) 0%, #a14436 12%, var(--sky-glow) 26%, #7a4660 38%, var(--sky-glow) 52%, var(--sky-warm) 64%, #d9592a 74%, #5a2a1f 84%, var(--sea) 100%);
  }
  .page {
    position: absolute; left: 151px; top: 22px; width: 747px; height: 1157px;
    background: var(--panel);
    border-radius: 3px;
  }
  .brand {
    position: absolute; left: 22px; top: 33px;
    display: flex; align-items: center; gap: 10px;
    font-size: 16px; font-weight: 400; color: var(--text);
  }
  .brand-dot { width: 34px; height: 34px; border-radius: 50%; background: var(--accent); }
  .search {
    position: absolute; left: 514px; top: 37px; width: 212px; height: 22px;
    border: 1px solid var(--line); border-radius: 3px;
    font-size: 10.5px; color: #b8b3b3; padding: 3px 10px;
  }
  .search svg { position: absolute; right: 8px; top: 5px; }
  .nav {
    position: absolute; left: 7px; top: 99px; width: 733px; height: 38px;
    background: var(--panel-deep); border-radius: 4px 4px 0 0;
    display: flex; align-items: center; padding-left: 51px;
    font-family: "Open Sans", Arial, sans-serif; font-size: 12.5px;
  }
  .nav a { color: var(--text); text-decoration: none; }
  .nav a.current { color: var(--accent); }
  .hero {
    position: absolute; left: 13px; top: 137px; width: 721px; height: 324px;
    background: linear-gradient(180deg, #e8ece9 0%, #d3dcd7 20%, #4f8a3a 32%, #3f7a2c 48%, #8a9a8c 58%, #6e7a73 80%, #5d665e 100%);
  }
  .dots {
    position: absolute; left: 396px; top: 427px; width: 88px; height: 22px;
    background: rgba(40,40,40,0.85); border-radius: 11px;
    display: flex; justify-content: center; align-items: center; gap: 4px;
  }
  .dots span { width: 11px; height: 11px; border-radius: 50%; border: 1.5px solid #ddd; }
  .dots span.on { background: var(--accent); border-color: #ddd; }
  .welcome {
    position: absolute; left: 7px; top: 461px; width: 733px; height: 174px;
    background: var(--panel-deep);
    border-radius: 0 0 40% 40% / 0 0 10px 10px;
    text-align: center;
  }
  .welcome h1 {
    font-family: "Roboto", Arial, sans-serif; font-weight: 700; font-size: 22px;
    color: var(--accent); margin-top: 33px;
  }
  .welcome p {
    font-size: 11.2px; line-height: 17px; color: var(--muted);
    margin: 14px 14px 0; 
  }
  .card {
    position: absolute; top: 706px; width: 217px; height: 226px;
    background: var(--card); border-radius: 4px;
    text-align: center;
  }
  .card-top { position: absolute; left: 0; top: -35px; }
  .card-icon {
    position: absolute; left: 82px; top: -12px; width: 54px; height: 54px;
    border-radius: 50%; background: #3a3a3a;
  }
  .card h2 {
    font-family: "Roboto", Arial, sans-serif; font-weight: 700; font-size: 15px;
    line-height: 16px; margin-top: 76px;
  }
  .card p {
    font-size: 11px; line-height: 15.3px; color: #bdb8b6;
    margin: 18px 16px 0;
  }
  .footer { position: absolute; top: 1010px; font-size: 12px; }
  .label { font-size: 9.5px; font-weight: 600; letter-spacing: 0.2px; }
  .links { display: grid; grid-template-columns: 79px 80px; row-gap: 3px; margin-top: 4px; }
  .links span { font-size: 12.5px; line-height: 15.5px; }
  .contact { font-size: 12.5px; line-height: 16.5px; margin-top: 3px; }
  .msg-btn {
    display: inline-block; margin-top: 12px; background: var(--accent);
    font-size: 10.5px; font-weight: 600; padding: 3px 11px; border-radius: 11px;
  }
  .social { display: flex; gap: 4px; margin-top: 10px; }
  .social span { width: 23px; height: 23px; border-radius: 50%; border: 1.5px solid #fff; }
  .copyright {
    position: absolute; left: 0; right: 0; top: 1131px; text-align: center;
    font-size: 10.5px; color: #a9a4a4;
  }
</style>
</head>
<body>
  <div class="backdrop" role="img" aria-label="Repeating photo of a fiery sunset sky over the sea with rocky sea stacks"></div>

  <main class="page">
    <header>
      <div class="brand"><span class="brand-dot"></span>Riverleaf Trust</div>
      <div class="search">Search
        <svg width="10" height="10" viewBox="0 0 10 10"><circle cx="4" cy="4" r="3" fill="none" stroke="#ccc" stroke-width="1.3"/><line x1="6.3" y1="6.3" x2="9" y2="9" stroke="#ccc" stroke-width="1.3"/></svg>
      </div>
      <nav class="nav">
        <a class="current" href="#" style="margin-right:48px">HOME</a>
        <a href="#" style="margin-right:48px">ABOUT</a>
        <a href="#" style="margin-right:48px">EXPLORE</a>
        <a href="#" style="margin-right:48px">CHALLENSES</a>
        <a href="#" style="margin-right:48px">SOLUTIONS</a>
        <a href="#" style="margin-right:48px">EVENTS</a>
        <a href="#">NEWS</a>
      </nav>
    </header>

    <div class="hero" role="img" aria-label="Slideshow photo of a child swimming in a lake with green trees on the shore"></div>
    <div class="dots"><span class="on"></span><span></span><span></span><span></span><span></span></div>

    <section class="welcome">
      <h1>Welcome to Comapny Name</h1>
      <p>Lorem ipsum dolor sit amet, consectetur adipiscing elit, sed do eiusmod tempor incididunt ut labore et dolore magna aliqua. Ut enim ad minim veniam, quis nostrud exercitation ullamco laboris nisi ut aliquip ex ea commodo consequat. Duis aute irure dolor in reprehenderit in voluptate velit esse cillum dolore eu fugiat nulla pariatur. Excepteur sint occaecat cupidatat non proident, sunt in culpa qui officia deserunt mollit anim id est laborum.</p>
    </section>

    <section class="card" style="left:29px">
      <svg class="card-top" width="217" height="42" viewBox="0 0 217 42"><path d="M0 38 H64 C72 38 70 5 108.5 5 C147 5 145 38 153 38 H217" fill="none" stroke="var(--accent)" stroke-width="5"/></svg>
      <div class="card-icon" role="img" aria-label="Volunteer icon"></div>
      <h2>Volunteer<br>Volunteer Wmus</h2>
      <p>Lorem ipsum dolor sit amet, consectetur adipiscing elit, sed do eiusmod tempor incididunt ut labore et dolore magna aliqua. Ut enim ad minim veniam.</p>
    </section>
    <section class="card" style="left:265px">
      <svg class="card-top" width="217" height="42" viewBox="0 0 217 42"><path d="M0 38 H64 C72 38 70 5 108.5 5 C147 5 145 38 153 38 H217" fill="none" stroke="var(--accent)" stroke-width="5"/></svg>
      <div class="card-icon" role="img" aria-label="Donate button icon with pointing hand"></div>
      <h2>Spport<br>Our Work</h2>
      <p>Lorem ipsum dolor sit amet, consectetur adipiscing elit, sed do eiusmod tempor incididunt ut labore et dolore magna aliqua. Ut enim ad minim veniam.</p>
    </section>
    <section class="card" style="left:501px">
      <svg class="card-top" width="217" height="42" viewBox="0 0 217 42"><path d="M0 38 H64 C72 38 70 5 108.5 5 C147 5 145 38 153 38 H217" fill="none" stroke="var(--accent)" stroke-width="5"/></svg>
      <div class="card-icon" role="img" aria-label="Protest group with signs icon"></div>
      <h2>Make Your<br>Voice Heard</h2>
      <p>Lorem ipsum dolor sit amet, consectetur adipiscing elit, sed do eiusmod tempor incididunt ut labore et dolore magna aliqua. Ut enim ad minim veniam.</p>
    </section>

    <footer>
      <div class="footer" style="left:55px">
        <div class="label">QUICK LINKS</div>
        <div class="links">
          <span>Home</span><span>Solutions</span>
          <span>About</span><span>Events</span>
          <span>Explore</span><span>News</span>
          <span>Challenses</span>
        </div>
      </div>

      <div class="footer" style="left:250px">
        <svg width="24" height="24" viewBox="0 0 24 24" style="position:absolute;left:0;top:4px"><path d="M5 3 L9 3 L10.5 8 L8 9.5 C9.5 13 11 14.5 14.5 16 L16 13.5 L21 15 L21 19 C21 20 20 21 19 21 C10 20.5 3.5 14 3 5 C3 4 4 3 5 3 Z" fill="none" stroke="#fff" stroke-width="1.3"/></svg>
        <div style="margin-left:37px">
          <div class="label">CALL</div>
          <div class="contact">1-000-000-0000</div>
        </div>
        <svg width="20" height="26" viewBox="0 0 20 26" style="position:absolute;left:6px;top:50px"><path d="M10 24 C4 16 2 12 2 9 A8 8 0 0 1 18 9 C18 12 16 16 10 24 Z" fill="none" stroke="#fff" stroke-width="1.3"/><circle cx="10" cy="9" r="3" fill="none" stroke="#fff" stroke-width="1.3"/></svg>
        <div style="margin-left:37px;margin-top:12px">
          <div class="label">VISIT</div>
          <div class="contact">Your Company LTD.<br>Street Name, 000000<br>City Name</div>
        </div>
      </div>

      <div class="footer" style="left:469px">
        <svg width="24" height="24" viewBox="0 0 24 24" style="position:absolute;left:0;top:2px"><path d="M3 21 L4.5 15.5 L17 3 L21 7 L8.5 19.5 Z M15 5 L19 9 M4.5 15.5 L8.5 19.5" fill="none" stroke="#fff" stroke-width="1.3"/></svg>
        <div style="margin-left:37px">
          <div class="label">WRITE</div>
          <div class="contact">info@yourdomain.com</div>
          <div class="msg-btn">MESSAGE US</div>
          <div class="social" aria-label="Social links">
            <span></span><span></span><span></span><span></span><span></span><span></span><span></span>
          </div>
        </div>
      </div>
    </footer>

    <div class="copyright">© 2015&nbsp; Comapny Name, All Rights Reserved</div>
  </main>
</body>
</html>
```